Brevanor Inc. Website

We need a website design for a new company based in Montreal, Canada. Our company offers professional services in planning & scheduling for major construction projects in varying industries. The main colors to be used are black & red (same as in logo). The final design should convey professionalism, precision, and excellence. The following are examples of what the website layout could look like: https://www.quilvardo.ca/, https://7496.ca/, https://lumavikt.ca/, https://www.dremorhext.com/en. Avoid using stock videos or photos with people in it.
Target audience are multi-national clients looking to hire a firm to manage their construction projects. Target market is Mining & Metals
Mining & Metalurgy, Hydroelectricity, Infrastructure
1 page

```html
<!DOCTYPE html>
<html lang="en">
<head>
<meta charset="utf-8">
<title>Brevanor Inc.</title>
<link href="https://fonts.googleapis.com/css2?family=Poppins:wght@400;500;600;700&display=swap" rel="stylesheet">
<style>
:root{
  --red:#9b0a1a;
  --orange:#f29a12;
  --ink:#2a2a2a;
  --dark:#333438;
  --header-bg:#edf0f6;
  --section-bg:#e7eaf1;
  --panel:#c9ccd4;
  --white:#ffffff;
}
*{box-sizing:border-box;margin:0;padding:0}
html,body{width:1200px;height:1200px;overflow:hidden;background:var(--white);font-family:'Poppins',sans-serif;color:var(--ink)}
.page{position:absolute;left:329px;top:0;width:569px;height:1196px}
.block{position:absolute;left:0;width:569px}

.site-header{top:1px;height:51px;background:var(--header-bg)}
.brand{position:absolute;display:flex;align-items:center;gap:4px;font-weight:700;color:var(--red);font-size:12px}
.brand-dot{width:9px;height:9px;border-radius:50%;background:var(--red)}
.site-header .brand{left:33px;top:17px}
.nav{position:absolute;left:206px;top:18px;display:flex;gap:10px;font-size:7px}

.hero{top:52px;height:234px;background:linear-gradient(180deg,#2d4f9a 0%,#4a5f94 35%,#7a5f6a 60%,#2a2528 85%,#1c1a1c 100%)}
.about{top:291px;height:233px;background:linear-gradient(180deg,#b9cbe0 0%,#a8a6a0 35%,#8a6848 60%,#4d3a2c 85%,#2b2420 100%)}
.section-title{position:absolute;left:49px;width:169px;background:var(--red);color:var(--white);font-weight:400;padding-left:12px;line-height:1.05}
.hero .section-title{top:23px;height:40px;font-size:18.5px;padding-top:1px}
.hero .section-title em{font-style:normal;color:var(--orange)}
.about .section-title{top:10px;height:20px;font-size:17px}
.rule{position:absolute;left:51px;width:468px;height:1px;background:var(--red)}
.copy{position:absolute;left:62px;width:444px;font-size:6.8px;line-height:10px;text-align:center}
.copy p{margin-bottom:7px}
.copy b{font-weight:600}
.hero .copy{top:70px;color:#f3f3f3}
.about .copy{top:41px;color:#222}
.btn{position:absolute;background:var(--dark);color:var(--white);font-size:6.8px;text-align:center;line-height:14px;height:14px}
.about .btn{left:225px;top:144px;width:118px}

.contact{top:530px;height:245px;background:var(--section-bg)}
.office-art{position:absolute;left:49px;top:25px;width:230px;height:216px;border:1px solid var(--red);background:linear-gradient(180deg,#f2f5fa 0%,#dfe6f0 45%,#6f84a3 75%,#a9bdd6 100%)}
.form-panel{position:absolute;left:290px;top:25px;width:229px;height:215px;background:var(--panel);border:1px solid #8f9198;border-top:2px solid #555}
.form-panel h2{position:absolute;left:21px;top:20px;font-size:14px;font-weight:400;color:#222}
.field-label{position:absolute;left:21px;font-size:6.5px;font-weight:600;color:#f2f2f2}
.field-hint{position:absolute;left:21px;font-size:6px;color:#e0e2e6}
.field-line{position:absolute;left:21px;width:187px;height:1px;background:#e8e9ec}
.field-box{position:absolute;left:21px;top:121px;width:187px;height:36px;background:#eef0f4;border-radius:2px}
.form-panel .btn{left:70px;top:172px;width:89px;border-radius:5px}

.services{top:778px;height:333px;background:linear-gradient(180deg,#d7d8dc 0%,#a9aaae 35%,#6f7074 70%,#3a3b3e 100%)}
.services .section-title{left:5px;top:10px;width:168px;height:20px;font-size:17px;padding-left:49px}
.services .rule{left:5px;top:29px;width:558px}
.card{position:absolute;top:36px;width:179px;height:217px;background:var(--white);text-align:center}
.card-art{position:absolute;left:9px;top:11px;width:160px;height:126px}
.card h3{position:absolute;left:0;width:100%;top:147px;font-size:6.8px;font-weight:600}
.card ul{position:absolute;left:0;width:100%;top:157px;list-style:none;font-size:6.8px;line-height:10px}
.card ul li::before{content:"✔";font-size:6px;margin-right:1px}
.card .btn{left:44px;top:194px;width:90px;border-left:3px solid var(--red);border-right:3px solid var(--red)}

.site-footer{top:1113px;height:83px;background:var(--red);overflow:hidden}
.site-footer svg{position:absolute;left:0;top:0}
.site-footer .brand{left:49px;top:30px}
.foot-col{position:absolute;top:19px;font-size:4.8px;line-height:7.6px;color:#f0cfd3}
.foot-col strong{color:var(--white);font-weight:500}
.socials{position:absolute;left:469px;top:25px;display:flex;gap:3px}
.socials span{width:6px;height:6px;border-radius:50%;background:#e8e8e8}
.legal{position:absolute;left:333px;top:68px;font-size:4.8px;font-weight:600;color:var(--white)}
</style>
</head>
<body>
<div class="page">

  <header class="block site-header">
    <div class="brand"><span class="brand-dot"></span>Brevanor</div>
    <nav class="nav"><span>Home</span><span>About Us</span><span>Contact Us</span></nav>
  </header>

  <section class="block hero" role="img" aria-label="Construction site with tower cranes against a dusk sky">
    <h1 class="section-title">Planning &amp;<br><em>Scheduling.</em></h1>
    <div class="copy">
      <p><b>Lorem ipsum dolor sit amet</b>, consectetur adipiscing elit. Sed a lacus dolor. Vestibulum ante ipsum primis in faucibus orci luctus et ultrices posuere cubilia curae; Ut leo neque, ullamcorper sed nisi non, finibus imperdiet diam. Proin interdum vulputate velit. Proin interdum in nisi vel consectetur.</p>
      <p><b>Lorem ipsum dolor sit amet</b>Suspendisse placerat, mi ornare cursus semper, est risus vestibulum leo, eu condimentum nunc quam at dui. Curabitur posuere ut ante id vehicula. Morbi at luctus purus. Praesent venenatis neque ac gravida consequat. Integer nibh purus, porttitor at aliquam eget, fringilla sit amet lacus. Pellentesque mattis ultrices eleifend. Aenean feugiat, arcu ac facilisis interdum, lacus mauris dignissim est, nec vestibulum orci nisl eget nibh. Sed auctor tortor quis ligula rutrum, vitae iaculis massa fermentum. Vestibulum eget ipsum posuere, rutrum nulla a, faucibus libero. Aliquam erat volutpat. Etiam eleifend ex lectus, at varius nibh facilisis non.</p>
    </div>
    <div class="rule" style="top:180px"></div>
  </section>

  <section class="block about" role="img" aria-label="Building interior under construction with timber and scaffolding">
    <h2 class="section-title">About US</h2>
    <div class="rule" style="top:29px;left:218px;width:301px"></div>
    <div class="copy">
      <p><b>Lorem ipsum dolor sit amet</b>, consectetur adipiscing elit. Sed a lacus dolor. Vestibulum ante ipsum primis in faucibus orci luctus et ultrices posuere cubilia curae; Ut leo neque, ullamcorper sed nisi non, finibus imperdiet diam. Proin interdum vulputate velit. Proin interdum in nisi vel consectetur.</p>
      <p><b>Lorem ipsum dolor sit amet</b>Suspendisse placerat, mi ornare cursus semper, est risus vestibulum leo, eu condimentum nunc quam at dui. Curabitur posuere ut ante id vehicula. Morbi at luctus purus. Praesent venenatis neque ac gravida consequat. Integer nibh purus, porttitor at aliquam eget, fringilla sit amet lacus. Pellentesque mattis ultrices eleifend. Aenean feugiat, arcu ac facilisis interdum, lacus mauris dignissim est, nec vestibulum orci nisl eget nibh. Sed auctor tortor quis ligula rutrum, vitae iaculis massa fermentum. Vestibulum eget ipsum posuere, rutrum nulla a, faucibus libero. Aliquam erat volutpat. Etiam eleifend ex lectus, at varius nibh facilisis non.</p>
    </div>
    <div class="btn">Contact Us</div>
    <div class="rule" style="top:173px"></div>
  </section>

  <section class="block contact">
    <div class="office-art" role="img" aria-label="Illustration of a bright office with desks, monitors and a plant"></div>
    <form class="form-panel">
      <h2>Contact Us</h2>
      <span class="field-label" style="top:43px">Name:</span>
      <span class="field-hint" style="top:57px">Enter Name</span>
      <div class="field-line" style="top:67px"></div>
      <span class="field-label" style="top:79px">Phone:</span>
      <span class="field-hint" style="top:93px">Enter phone</span>
      <div class="field-line" style="top:102px"></div>
      <span class="field-label" style="top:114px">Message:</span>
      <div class="field-box"></div>
      <div class="btn">Send message</div>
    </form>
  </section>

  <section class="block services">
    <h2 class="section-title">Services</h2>
    <div class="rule"></div>
    <article class="card" style="left:5px">
      <div class="card-art" role="img" aria-label="Laptop showing a project schedule chart" style="background:linear-gradient(135deg,#3f6fd6,#1d3f9a)"></div>
      <h3>Projects Management</h3>
      <ul><li>Lorem ipsum dolor sit amet</li><li>Lorem ipsum dolor sit amet</li><li>Lorem ipsum dolor sit amet</li></ul>
      <div class="btn">Explore</div>
    </article>
    <article class="card" style="left:194px">
      <div class="card-art" role="img" aria-label="Industrial plant overlaid with a technical network graphic" style="background:linear-gradient(135deg,#6a6a6a,#1f1f22 60%,#8a7040)"></div>
      <h3>Projects Control</h3>
      <ul><li>Lorem ipsum dolor sit amet</li><li>Lorem ipsum dolor sit amet</li><li>Lorem ipsum dolor sit amet</li></ul>
      <div class="btn">Explore</div>
    </article>
    <article class="card" style="left:384px">
      <div class="card-art" role="img" aria-label="Apartment buildings under construction with a crane" style="background:linear-gradient(180deg,#5a6878 0%,#c7ccd3 45%,#e4e2dc 65%,#c59a6a 100%)"></div>
      <h3>Projects Construstions</h3>
      <ul><li>Lorem ipsum dolor sit amet</li><li>Lorem ipsum dolor sit amet</li><li>Lorem ipsum dolor sit amet</li></ul>
      <div class="btn">Explore</div>
    </article>
  </section>

  <footer class="block site-footer">
    <svg width="569" height="83" viewBox="0 0 569 83" aria-hidden="true">
      <polygon points="0,0 150,0 122,83 0,83" fill="#edf0f6"/>
      <polygon points="150,0 158,0 130,83 122,83" fill="#1a1a1a"/>
    </svg>
    <div class="brand"><span class="brand-dot"></span>Brevanor</div>
    <div class="foot-col" style="left:222px">
      <strong>Detail address</strong><br>Lorem ipsum<br>Lorem ipsum<br>Lorem ipsum<br>&#9990; (00) 0000 0000<br>&#9993; example@brevanor.com
    </div>
    <div class="foot-col" style="left:382px">
      <strong>Menu</strong><br>Home<br>About Us<br>Contact Us
    </div>
    <div class="socials"><span></span><span></span><span></span></div>
    <div class="legal">BREVANOR | 2023 | All Rights Reserved</div>
  </footer>

</div>
</body>
</html>
```